QuintaraHC Postcard Design

We need a postcard design for our home health care company in Albuquerque, NM. The services we offer are home healthcare services. I included a digital brochure for reference.

Target Market(s)

elderly people and/or people looking for home health services

Industry/Entity Type

Home Health Care

Requirements
Must have
• Must have our moto "Bringing Quality Care Home". Must have our contact information including website. Must have our logo.
Nice to have
• picture of caregiver and client or picture of elderly couple

```html
<!DOCTYPE html>
<html lang="en">
<head>
<meta charset="utf-8">
<title>Quintara Home Care Postcard</title>
<link rel="stylesheet" href="https://fonts.googleapis.com/css2?family=Arimo:wght@400&display=swap">
<style>
  :root {
    --page-bg: #d9dcdb;
    --card-top: #f6f6f6;
    --card-bottom: #e6e6e6;
    --ink: #1c1c1c;
    --brand-blue: #1f5ea8;
    --rule: #cfcfcf;
    --stamp: #dcdcdc;
  }
  * { margin: 0; padding: 0; box-sizing: border-box; }
  html, body {
    width: 1200px;
    height: 800px;
    overflow: hidden;
    background: var(--page-bg);
    font-family: "Arimo", Arial, sans-serif;
  }
  .postcard {
    position: absolute;
    left: 75px;
    top: 50px;
    width: 1050px;
    height: 700px;
    background: linear-gradient(180deg, var(--card-top) 0%, var(--card-bottom) 100%);
    box-shadow: 0 6px 18px rgba(0,0,0,0.12);
  }
  .brand {
    position: absolute;
    left: 120px;
    top: 44px;
    display: flex;
    align-items: center;
    gap: 14px;
    color: var(--brand-blue);
    font-weight: 400;
  }
  .brand-dot {
    width: 30px;
    height: 30px;
    border-radius: 50%;
    background: var(--brand-blue);
  }
  .brand-name {
    font-size: 38px;
    line-height: 1;
    letter-spacing: 1px;
  }
  .brand-sub {
    display: block;
    font-size: 18px;
    letter-spacing: 6px;
    margin-top: 8px;
  }
  .contact {
    position: absolute;
    left: 445px;
    top: 30px;
    font-size: 18px;
    line-height: 26px;
    color: var(--ink);
    font-style: normal;
  }
  .contact .web { margin-top: 12px; display: block; }
  .stamp-box {
    position: absolute;
    left: 818px;
    top: 36px;
    width: 118px;
    height: 124px;
    background: var(--stamp);
  }
  .message {
    position: absolute;
    left: 121px;
    top: 206px;
    width: 365px;
    font-size: 18px;
    line-height: 30px;
    color: var(--ink);
  }
  .message p + p { margin-top: 12px; }
  .divider {
    position: absolute;
    left: 512px;
    top: 200px;
    width: 1px;
    height: 370px;
    background: var(--rule);
  }
  .address-lines {
    position: absolute;
    left: 592px;
    top: 344px;
    width: 318px;
  }
  .address-lines span {
    display: block;
    height: 1px;
    background: var(--rule);
    margin-bottom: 57px;
  }
</style>
</head>
<body>
  <main class="postcard">
    <div class="brand">
      <span class="brand-dot"></span>
      <div>
        <span class="brand-name">QUINTARA</span>
        <span class="brand-sub">HOME CARE</span>
      </div>
    </div>

    <address class="contact">
      2740 Sandia Ridge Blvd NE<br>
      Albuquerque, NM 87110<br>
      505.555.0182
      <span class="web">www.QuintaraHomeCare.com</span>
    </address>

    <div class="stamp-box"></div>

    <section class="message">
      <p>Whether it’s injury, illness or just life changes, sometimes we are not able to keep up with household chores like we used to. Quintara Home Care can help.</p>
      <p>Quintara Home Care is New Mexico’s premier home health care agency and is locally owned and operated.</p>
      <p>Our companions, personal care attendants and homemakers are ready to assist you in living safely, independently and comfortably at home.</p>
      <p>Bring Quality Care Home.</p>
    </section>

    <div class="divider"></div>

    <div class="address-lines">
      <span></span><span></span><span></span><span></span>
    </div>
  </main>
</body>
</html>
```